Web Design for Meadowfield Turf Crew

Meadowfield Turf Crew needs the photoshop files for a simple, clean and professional web design. I need a home and subpage design, although they can be very similar. See pagestridehub.com for a desired layout, although I'd like to see more design than shown on that site. The goal of the site is to attract both lawn maintenance/landscape customers and build a partner network of consultants that serve the US market. The following are needed:

- home and subpage design
- page: Home, Services, Locations, Consultants, FAQ, Contact
- if subpages have header photo, need to include 5 different header photos for each page
- favicon
Updates

I'll award the design based on the homepage concept. The minor subpage changes and other elements can be worked out in the workroom stage. Thanks, Trent

Industry/Entity Type

It Professional

```html
<!DOCTYPE html>
<html lang="en">
<head>
<meta charset="utf-8">
<title>Meadowfield Turf Crew</title>
<link href="https://fonts.googleapis.com/css2?family=Roboto:wght@300;400;500&display=swap" rel="stylesheet">
<style>
:root{
  --green:#7cae1e;
  --green-dark:#6a9a14;
  --slate:#5f5f62;
  --panel:#616163;
  --text:#4a4a4a;
  --muted:#888;
  --line:#d6d6d6;
  --white:#fff;
  --black:#000;
}
*{box-sizing:border-box;margin:0;padding:0}
html,body{width:1200px;height:1128px;overflow:hidden}
body{font-family:'Roboto',Arial,sans-serif;background:var(--white);position:relative;color:var(--text)}
.abs{position:absolute}
.top-rule{left:0;top:0;width:1200px;height:4px;background:var(--green)}
.brand{left:200px;top:22px;height:44px;display:flex;align-items:center;gap:10px}
.brand-mark{width:36px;height:36px;border:3px solid var(--slate);border-radius:6px}
.brand-name{font-size:24px;font-weight:400;color:var(--slate);letter-spacing:0.5px}
.search{left:707px;top:26px;width:154px;height:22px;border:1px solid var(--line);font-size:8px;color:#aaa;padding:6px 6px}
.search-btn{left:861px;top:26px;width:22px;height:22px;background:var(--slate)}
.social-sq{top:26px;width:22px;height:22px;background:var(--green)}
.contact-line{top:57px;font-size:10px;color:var(--muted);display:flex;align-items:center;gap:5px}
.nav{left:0;top:82px;width:1200px;height:48px;background:var(--green)}
.nav-item{top:82px;height:48px;line-height:48px;font-size:10px;color:var(--white);text-align:center;transform:translateX(-50%)}
.nav-home{left:200px;top:82px;width:106px;height:48px;background:var(--slate);color:var(--white);font-size:10px;line-height:48px;text-align:center}
.hero{left:0;top:130px;width:1200px;height:464px;background:linear-gradient(180deg,#b7bcc0 0%,#c9c3b1 35%,#4c6a3c 55%,#6fa22e 78%,#5c9523 100%)}
.hero-caption{left:720px;top:293px;width:278px;height:65px;background:var(--green);color:var(--white);font-size:24px;font-weight:400;padding:18px 24px}
.hero-arrow{top:294px;width:43px;height:56px;background:rgba(40,40,40,.85);display:flex;align-items:center;justify-content:center}
.dot{top:569px;width:10px;height:10px;border-radius:50%;background:var(--white);border:1px solid #888}
.dot.active{background:var(--green)}
.h2{font-size:20px;font-weight:400;color:var(--green)}
.copy{font-size:9.6px;line-height:19.2px;color:var(--text)}
.read-more{font-size:9.6px;color:var(--black)}
.card-img{width:249px;height:129px;border:1px solid #ccc}
.card-label{width:247px;height:21px;background:rgba(80,80,80,.7);color:var(--white);font-size:11.5px;line-height:21px;padding-left:8px}
.card-more{font-size:9.6px;color:var(--green)}
.form-panel{left:758px;top:652px;width:240px;height:368px;background:var(--panel)}
.field{left:768px;width:221px;background:var(--white);border:1px solid #ccc;font-size:9.6px;color:var(--muted);padding:0 10px;display:flex;align-items:center}
.field.area{align-items:flex-start;padding-top:8px}
.submit{left:922px;top:982px;width:67px;height:28px;background:var(--green);color:var(--white);font-size:12px;line-height:28px;text-align:center;border:1px solid #9bcc3c}
.footer{left:0;top:1058px;width:1200px;height:70px;background:var(--black)}
.footer-copy{left:199px;top:1086px;font-size:12px;color:var(--white)}
.foot-circle{top:1077px;width:30px;height:30px;border-radius:50%;background:#d8d8d8}
</style>
</head>
<body>
<div class="abs top-rule"></div>

<div class="abs brand">
  <div class="brand-mark"></div>
  <span class="brand-name">Meadowfield Turf Crew</span>
</div>

<div class="abs search">Search ...</div>
<div class="abs search-btn">
  <svg width="22" height="22" viewBox="0 0 22 22"><circle cx="10" cy="10" r="4" fill="none" stroke="#fff" stroke-width="1.6"/><line x1="13" y1="13" x2="16" y2="16" stroke="#fff" stroke-width="1.8"/></svg>
</div>
<div class="abs social-sq" style="left:884px" aria-label="Social link"></div>
<div class="abs social-sq" style="left:907px" aria-label="Social link"></div>
<div class="abs social-sq" style="left:930px" aria-label="Social link"></div>
<div class="abs social-sq" style="left:953px" aria-label="Social link"></div>
<div class="abs social-sq" style="left:976px" aria-label="Feed link"></div>

<div class="abs contact-line" style="left:790px">
  <svg width="8" height="8" viewBox="0 0 10 10"><path d="M2 1l2 2-1 1.5c.8 1.5 1.5 2.2 3 3L7.5 6l2 2-1.5 1.5C4.5 9 1 5.5.5 2.5z" fill="#999"/></svg>
  5550 2187
</div>
<div class="abs contact-line" style="left:862px">
  <svg width="10" height="8" viewBox="0 0 10 8"><rect width="10" height="8" fill="#999"/><path d="M0 0l5 4 5-4" fill="none" stroke="#fff" stroke-width="1"/></svg>
  hello@meadowfieldturf.com
</div>

<nav>
  <div class="abs nav"></div>
  <div class="abs nav-home">Home</div>
  <div class="abs nav-item" style="left:372px">Services</div>
  <div class="abs nav-item" style="left:499px">Locations</div>
  <div class="abs nav-item" style="left:636px">Consultants</div>
  <div class="abs nav-item" style="left:760px">FAQ</div>
  <div class="abs nav-item" style="left:882px">Contact Us</div>
</nav>

<div class="abs hero" role="img" aria-label="Photo of a ride-on mower on a green golf fairway at dusk, tree line and cloudy sky"></div>
<div class="abs hero-caption">lawn maintenance</div>
<div class="abs hero-arrow" style="left:0">
  <svg width="16" height="22" viewBox="0 0 16 22"><path d="M12 2L4 11l8 9" fill="none" stroke="#fff" stroke-width="3.5"/></svg>
</div>
<div class="abs hero-arrow" style="left:1148px;width:52px">
  <svg width="16" height="22" viewBox="0 0 16 22"><path d="M4 2l8 9-8 9" fill="none" stroke="#fff" stroke-width="3.5"/></svg>
</div>
<div class="abs dot active" style="left:581px"></div>
<div class="abs dot" style="left:597px"></div>
<div class="abs dot" style="left:614px"></div>

<h2 class="abs h2" style="left:200px;top:617px">Welcome To Meadowfield Turf Crew</h2>
<p class="abs copy" style="left:200px;top:650px;width:530px">Lorem ipsum dolor sit amet, consectetuer adipiscing elit, sed diam nonummy nibh euismod tincidunt ut laoreet dolore magna aliquam erat volutpat. Ut wisi enim ad minim veniam, quis nostrud exerci tation ullamcorper suscipit lobortis nisl ut aliquip ex ea commodo consequat. Lorem ipsum dolor sit amet, consectetuer adipiscing elit, sed diam nonummy nibh euismod tincidunt ut laoreet dolore magna aliquam erat volutpat.</p>
<span class="abs read-more" style="left:199px;top:729px">Read More +</span>

<h2 class="abs h2" style="left:200px;top:758px">Services</h2>
<svg class="abs" style="left:698px;top:767px" width="26" height="10" viewBox="0 0 26 10"><path d="M6 0v10L0 5z" fill="#333"/><path d="M18 0v10l6-5z" fill="#333"/></svg>

<div class="abs card-img" style="left:200px;top:794px;background:linear-gradient(180deg,#5d8a2c,#86bb3b 60%,#9a9a9a)" role="img" aria-label="Photo of a worker on a red ride-on mower beside a driveway"></div>
<div class="abs card-label" style="left:201px;top:902px">Lawn Clean</div>
<p class="abs copy" style="left:200px;top:930px;width:252px">Lorem ipsum dolor sit amet, consectetuer adipiscing elit, sed diam nonummy nibh euismod tincidunt ut laoreet dolore magna aliquam erat volutpat.uismod tincidunt ut laoreet dolore magna aliquam erat volutpat.</p>
<span class="abs card-more" style="left:200px;top:1011px">Read More +</span>

<div class="abs card-img" style="left:477px;top:794px;background:linear-gradient(180deg,#7aab3a,#8fbf48 60%,#8a8a7a)" role="img" aria-label="Photo of a worker in a red jacket pushing a mower across grass"></div>
<div class="abs card-label" style="left:478px;top:902px">Lawn Clean</div>
<p class="abs copy" style="left:477px;top:930px;width:252px">Lorem ipsum dolor sit amet, consectetuer adipiscing elit, sed diam nonummy nibh euismod tincidunt ut laoreet dolore magna aliquam erat volutpat.uismod tincidunt ut laoreet dolore magna aliquam erat volutpat.</p>
<span class="abs card-more" style="left:477px;top:1011px">Read More +</span>

<h2 class="abs h2" style="left:757px;top:617px">Start Your Movement...</h2>
<div class="abs form-panel"></div>
<div class="abs field" style="top:665px;height:34px">Name</div>
<div class="abs field" style="top:707px;height:34px">Email</div>
<div class="abs field" style="top:750px;height:34px">Phone</div>
<div class="abs field" style="top:793px;height:34px">Business Name</div>
<div class="abs field" style="top:838px;height:35px">Domain Name</div>
<div class="abs field area" style="top:881px;height:93px">Brief Description of Your Business *</div>
<div class="abs submit">Submit</div>

<footer>
  <div class="abs footer"></div>
  <div class="abs footer-copy">© 2014 Meadowfield Turf Crew. All Rights Reserved.</div>
  <div class="abs foot-circle" style="left:896px" aria-label="Social link"></div>
  <div class="abs foot-circle" style="left:932px" aria-label="Social link"></div>
  <div class="abs foot-circle" style="left:968px" aria-label="Social link"></div>
</footer>
</body>
</html>
```